Attractive door board for entrance beautysalon

Make an attractive design for a board that can be glued on the front door of a beauty salon. The salon location has no window in the front so I need something catchy and attractive. The door board contains a list of the services and the website: www.atelierkm.be, and the text "Enkel op afspraak, bel 0486317492"

Target Market(s)

woman between 16 and 99 years old

Industry/Entity Type

Beauty Salon

Font styles to use
Sans Serif

Requirements
Must have
• A very nice, attractive but sober design.
• It must have a classy Morvane, Lusa, ... chique design.
• The logo must be on it (in attachment)
• There must be the following list in it:
• Gelaatsverzorging
• Wimperverlenging
• Wimperlifting
• Suikerontharing
• Permanente Make Up
• Airbrush Tanning
• Manicure - Pedicure - Velura
• and then the website www.atelierkm.be, and the text "Enkel op afspraak, bel 0486317492"
Nice to have
• a catchy design,
• max. width can be 75 cm and max height 180 cm as it is a design for a board that will be glued on a door.
Should not have
• orchid flowers, buddha look a likes

```html
<!DOCTYPE html>
<html lang="nl">
<head>
<meta charset="utf-8">
<title>Atelier KM – deurbord varianten</title>
<link rel="stylesheet" href="https://fonts.googleapis.com/css2?family=Josefin+Sans:wght@300;400&family=Montserrat:wght@500;600&display=swap">
<style>
  :root {
    --canvas: #f4f4f4;
    --ink: #111111;
    --paper: #ffffff;
    --noir: #000000;
    --grijs: #dcdcdc;
    --zilver-dark: #8f9092;
    --zilver-mid: #c9cacb;
    --zilver-light: #f7f7f7;
    --shadow: rgba(0, 0, 0, 0.28);
  }
  * { box-sizing: border-box; margin: 0; padding: 0; }
  html, body {
    width: 1200px; height: 1200px; overflow: hidden;
    background: var(--canvas);
  }
  .sheet {
    width: 1200px; height: 1200px;
    display: flex; align-items: center; justify-content: center; gap: 40px;
  }
  .board {
    width: 340px; height: 482px;
    display: flex; flex-direction: column;
    box-shadow: 0 2px 6px var(--shadow);
    font-family: "Montserrat", sans-serif;
    color: var(--ink);
  }
  .board__head {
    height: 194px;
    display: flex; flex-direction: column; align-items: center; justify-content: center;
    gap: 18px; padding-top: 40px;
  }
  .brand-name {
    font-family: "Josefin Sans", sans-serif;
    font-weight: 300;
    font-size: 24px;
    letter-spacing: 15px;
    margin-right: -15px;
    text-transform: uppercase;
  }
  .brand-sub {
    font-family: "Montserrat", sans-serif;
    font-weight: 600;
    font-size: 6.5px;
    letter-spacing: 6.3px;
    margin-right: -6.3px;
    text-transform: uppercase;
  }
  .services {
    flex: 1;
    background: var(--paper);
    list-style: none;
    display: flex; flex-direction: column; align-items: center; justify-content: center;
    gap: 11.5px;
  }
  .services li {
    font-weight: 600;
    font-size: 10.5px;
    letter-spacing: 2.6px;
    text-transform: uppercase;
    display: flex; align-items: center;
  }
  .services li::before {
    content: ""; width: 6px; height: 6px; border-radius: 50%;
    background: var(--ink); margin-right: 8px;
  }
  .board__foot {
    height: 80px;
    display: flex; flex-direction: column; align-items: center; justify-content: center;
    gap: 12px;
  }
  .site {
    font-weight: 600; font-size: 15px; letter-spacing: 3.6px;
  }
  .appointment {
    font-weight: 600; font-size: 7.5px; letter-spacing: 1.5px; text-transform: uppercase;
  }
  .appointment .phone { font-size: 11.5px; letter-spacing: 2.2px; }

  .board--noir .board__head,
  .board--noir .board__foot { background: var(--noir); color: var(--paper); }

  .board--grijs .board__head,
  .board--grijs .board__foot { background: var(--grijs); }

  .board--zilver .board__head,
  .board--zilver .board__foot {
    background: linear-gradient(140deg, var(--zilver-dark) 0%, var(--zilver-mid) 28%, var(--zilver-light) 48%, var(--zilver-mid) 62%, var(--zilver-dark) 100%);
  }
  .board--zilver .board__head { height: 242px; padding-top: 56px; }
  .board--zilver .services {
    gap: 7px;
    border-top: 2px solid var(--ink);
    border-bottom: 2px solid var(--ink);
  }
  .board--zilver .services li { font-size: 8.5px; letter-spacing: 2.2px; }
</style>
</head>
<body>
<main class="sheet">

  <section class="board board--noir">
    <header class="board__head">
      <div class="brand-name">Atelier KM</div>
      <div class="brand-sub">Schoonheidsinstituut</div>
    </header>
    <ul class="services">
      <li>Gelaatsverzorging</li>
      <li>Wimperverlenging</li>
      <li>Wimperlifting</li>
      <li>Suikerontharing</li>
      <li>Permanente make up</li>
      <li>Airbrush tanning</li>
      <li>Manicure - Pedicure - Velura</li>
    </ul>
    <footer class="board__foot">
      <div class="site">www.atelierkm.be</div>
      <div class="appointment">Enkel op afspraak, bel <span class="phone">0486317492</span></div>
    </footer>
  </section>

  <section class="board board--grijs">
    <header class="board__head">
      <div class="brand-name">Atelier KM</div>
      <div class="brand-sub">Schoonheidsinstituut</div>
    </header>
    <ul class="services">
      <li>Gelaatsverzorging</li>
      <li>Wimperverlenging</li>
      <li>Wimperlifting</li>
      <li>Suikerontharing</li>
      <li>Permanente make up</li>
      <li>Airbrush tanning</li>
      <li>Manicure - Pedicure - Velura</li>
    </ul>
    <footer class="board__foot">
      <div class="site">www.atelierkm.be</div>
      <div class="appointment">Enkel op afspraak, bel <span class="phone">0486317492</span></div>
    </footer>
  </section>

  <section class="board board--zilver">
    <header class="board__head">
      <div class="brand-name">Atelier KM</div>
      <div class="brand-sub">Schoonheidsinstituut</div>
    </header>
    <ul class="services">
      <li>Gelaatsverzorging</li>
      <li>Wimperverlenging</li>
      <li>Wimperlifting</li>
      <li>Suikerontharing</li>
      <li>Permanente make up</li>
      <li>Airbrush tanning</li>
      <li>Manicure - Pedicure - Velura</li>
    </ul>
    <footer class="board__foot">
      <div class="site">www.atelierkm.be</div>
      <div class="appointment">Enkel op afspraak, bel <span class="phone">0486317492</span></div>
    </footer>
  </section>

</main>
</body>
</html>
```